International IT and cyber security consulting company is looking to establish a web presence.

Halvern Ridge Advisory LLC provides IT, cyber security, risk, project management and data analytics consulting services worldwide. Our clients are both government and corporate. We are looking to establish a basic web presence with about 6 pages (Home, About Halvern, Our Experts, News and Events, Careers, Contact Us). The designs should set the look and feel of the site for further build out down the line. The final design should be straightforward and simple and allow us to convey information about our consulting services clearly.

Target Market(s)

Government and corporate clients or potential clients, job seekers.

Industry/Entity Type

Consulting

Contact Information for Business Card

The cards will have english on the front and arabic on the back. The design should be the same on both sides.

Coding

Number of Pages Required

Font styles to use
Serif
Sans Serif

Requirements
Must have
• The pages should be simple but visually appealing with a picture or graphic that is appropriate to the company or services we offer. Our name and logo should be branded throughout the design. While we are mostly an IT company we also have a line of business where we organize speaking events for VIPs so the website shouldn't overly emphasize our IT work.
Should not have
• No cartoons or drawings. The site should not have overly flashy or loud colors. We cater to a conservative set of clients so the site should match what they expect to see in an international consultancy's website. There should not be an overuse of the color orange because it can be hard on the eyes if it is used too much on the page. Also, please do not use graphics or pictures that use locks, keys, castles, shields etc since these are too commonly used in the cyber security industry.

```html
<!DOCTYPE html>
<html lang="en">
<head>
<meta charset="utf-8">
<title>Halvern Ridge Advisory LLC</title>
<link href="https://fonts.googleapis.com/css2?family=Cinzel:wght@400;500&family=Roboto:wght@400;500;700&family=Source+Sans+3:wght@400;600;700&display=swap" rel="stylesheet">
<style>
:root{
  --teal:#1ec4dd;
  --teal-dark:#15afc7;
  --ink:#111;
  --text:#666;
  --muted:#888;
  --light:#ededed;
  --footer:#161616;
  --white:#fff;
}
*{margin:0;padding:0;box-sizing:border-box}
html,body{width:1200px;height:3991px;overflow:hidden}
body{position:relative;background:var(--white);font-family:"Source Sans 3",sans-serif;color:var(--text)}
.abs{position:absolute}
a{text-decoration:none;color:inherit}

/* header */
.topbar{left:0;top:0;width:1200px;height:83px;background:var(--white)}
.brand-panel{left:0;top:0;width:370px;height:83px;background:#f1f1f1;clip-path:polygon(0 0,100% 0,340px 100%,0 100%)}
.brand{left:90px;top:14px;width:200px;font-family:"Source Sans 3",sans-serif;font-weight:600;font-size:19px;line-height:22px;color:#e07b3c;display:flex;gap:8px;align-items:flex-start}
.brand .dot{width:12px;height:12px;border-radius:50%;background:#e07b3c;margin-top:5px;flex:none}
.contact-item{top:18px;display:flex;align-items:center;gap:16px;font-size:13px;color:#555}
.contact-item .ic{width:46px;height:46px;border:2px solid var(--teal);border-radius:50%;display:flex;align-items:center;justify-content:center}
.contact-item b{display:block;font-size:15px;color:#222;font-weight:600;margin-top:3px}
.navbar{left:0;top:83px;width:1200px;height:47px;background:var(--teal)}
.nav{left:88px;top:96px;display:flex;gap:59px;font-size:16px;font-weight:600;color:var(--white)}
.nav .active{color:#111}
.social{top:99px;display:flex;gap:22px}
.social span{width:14px;height:14px;border-radius:50%;background:var(--white);display:block}

/* hero */
.hero{left:0;top:130px;width:1200px;height:523px;background:radial-gradient(ellipse at 65% 45%,#1f6b55 0%,#152455 35%,#0b1030 75%)}
.hero h1{left:90px;top:222px;font-family:"Cinzel",serif;font-weight:400;font-size:64px;line-height:60px;color:var(--white);letter-spacing:1px}
.btn{display:flex;align-items:center;justify-content:center;background:var(--teal);color:var(--white);border-radius:30px;font-family:"Roboto",sans-serif;font-weight:500}
.hero .btn{left:90px;top:366px;width:196px;height:52px;font-size:20px}
.dots{left:90px;top:538px;display:flex;gap:12px}
.dots span{width:11px;height:11px;border-radius:50%;background:var(--white)}
.dots span:first-child{background:var(--teal)}

/* services */
.service{top:694px;width:160px;text-align:center;font-size:15px;line-height:22px;color:#555}
.service svg{display:block;margin:0 auto 14px}
.divider{top:698px;width:1px;height:104px;background:#ddd}
.svc-card{left:922px;top:581px;width:186px;height:248px;background:var(--white);box-shadow:0 4px 14px rgba(0,0,0,.14);text-align:center;font-size:15px;line-height:22px;color:#333}
.svc-card .media{height:165px;background:linear-gradient(135deg,#2a4d7c,#6b8fb8 60%,#a9c3de)}
.svc-card p{padding-top:17px}

/* welcome */
.welcome{left:90px;top:900px;width:1020px;text-align:center}
.welcome h2{font-family:"Roboto",sans-serif;font-weight:500;font-size:40px;color:var(--ink);margin-bottom:22px}
.welcome p{font-size:13.5px;line-height:29px;color:#666;margin-bottom:28px}
.welcome .btn{width:196px;height:55px;margin:0 auto;font-size:20px}

/* about */
.about{left:0;top:1299px;width:614px;height:501px;background:var(--teal);color:var(--white);padding:90px 40px 0 90px}
.about h2{font-family:"Roboto",sans-serif;font-weight:400;font-size:38px;margin-bottom:22px}
.about p{font-size:15px;line-height:29.5px}
.about svg{margin-top:22px}
.about-photo{left:614px;top:1299px;width:586px;height:501px;background:linear-gradient(135deg,#e8ecef,#c7cfd6 50%,#8a7664)}

/* testimonials */
.section-title{width:1200px;left:0;text-align:center;font-family:"Roboto",sans-serif;font-weight:500;font-size:38px;color:var(--ink)}
.t-card{top:1945px;height:380px;background:var(--white);box-shadow:0 3px 10px rgba(0,0,0,.12);border-radius:0 0 14px 14px;overflow:hidden}
.t-card .media{height:282px;position:relative}
.t-card .quote{position:absolute;left:16px;right:16px;bottom:18px;color:var(--white);font-size:15px;line-height:26px}
.t-card .who{display:flex;gap:12px;padding:16px 10px 0;font-size:15px;color:#222}
.t-card .who i{display:block;font-size:14px;color:#777}
.t-card .av{width:42px;height:42px;border-radius:50%;background:#c7a48b;flex:none}
.t-card .date{font-size:10.5px;color:#555;padding:12px 10px 0}
.arrow{top:2134px;font-size:22px;color:#555}

/* ready */
.ready-photo{left:0;top:2412px;width:586px;height:500px;background:linear-gradient(135deg,#0f2a4a,#1e5c92 50%,#7fa6c9)}
.ready{left:586px;top:2412px;width:614px;height:500px;background:var(--light);padding:128px 0 0 90px}
.ready h2{font-family:"Roboto",sans-serif;font-weight:400;font-size:38px;line-height:50px;color:#222}
.ready p{font-size:15px;color:#444;margin:18px 0 38px}
.ready .btn{width:165px;height:49px;font-size:15px}

/* blog */
.post{top:3054px;width:329px}
.post .media{height:243px}
.post h3{font-family:"Roboto",sans-serif;font-weight:500;font-size:22px;line-height:31px;color:#222;margin:22px 0 16px}
.post .bar{width:32px;height:3px;background:var(--teal);margin-bottom:22px}
.post p{font-size:13.5px;line-height:26px;color:#555;margin-bottom:16px}
.post .more{font-family:"Roboto",sans-serif;font-weight:500;font-size:14px;color:var(--teal)}

/* footer */
.footer{left:0;top:3577px;width:1200px;height:414px;background:var(--footer)}
.f-col{top:3640px;color:#ddd;font-size:12px;line-height:28px}
.f-col h4{font-family:"Roboto",sans-serif;font-weight:500;font-size:17px;color:var(--white);margin-bottom:22px;line-height:20px}
.news{display:flex;gap:12px;margin-bottom:22px;line-height:18px}
.news .thumb{width:72px;height:56px;background:#8b7766;flex:none}
.news small{display:block;font-size:9px;margin-top:4px}
.f-links{line-height:28px}
.nl-form{display:flex;margin-top:14px}
.nl-form span{width:200px;height:48px;background:var(--white);color:#555;padding:16px 12px;line-height:16px}
.nl-form b{width:48px;height:48px;background:var(--teal);display:flex;align-items:center;justify-content:center}
.f-social{display:flex;gap:14px;margin-top:14px}
.f-social span{width:34px;height:34px;background:#2a2a2a;display:block}
.f-social span:nth-child(2){background:var(--teal)}
.c-line{border-bottom:1px solid #333;padding:10px 0;display:flex;gap:10px;line-height:20px}
.copyright{left:0;top:3962px;width:1200px;text-align:center;font-size:12px;color:#ddd}
</style>
</head>
<body>

<!-- header -->
<div class="abs topbar"></div>
<div class="abs brand-panel"></div>
<div class="abs brand"><span class="dot"></span><span>Halvern Ridge Advisory LLC</span></div>
<div class="abs contact-item" style="left:685px">
  <span class="ic"><svg width="18" height="18" viewBox="0 0 24 24"><path d="M6.6 10.8a15 15 0 0 0 6.6 6.6l2.2-2.2c.3-.3.7-.4 1-.2 1.1.4 2.3.6 3.6.6.6 0 1 .4 1 1V20c0 .6-.4 1-1 1A17 17 0 0 1 3 4c0-.6.4-1 1-1h3.5c.6 0 1 .4 1 1 0 1.3.2 2.5.6 3.6.1.3 0 .7-.2 1z" fill="#1ec4dd"/></svg></span>
  <span>Call Now:<b>+1 555 010 2040</b></span>
</div>
<div class="abs contact-item" style="left:927px">
  <span class="ic"><svg width="18" height="14" viewBox="0 0 18 14"><rect width="18" height="14" rx="2" fill="#1ec4dd"/><path d="M1 2l8 6 8-6" stroke="#fff" stroke-width="1.6" fill="none"/></svg></span>
  <span>Email:<br>hello@halvernridge.example</span>
</div>
<div class="abs navbar"></div>
<nav class="abs nav">
  <a class="active">Home</a><a>About Halvern</a><a>Our Experts</a><a>News And Events</a><a>Careers</a><a>Contact Us</a>
</nav>
<div class="abs social" style="left:1020px"><span></span><span></span><span></span></div>

<!-- hero -->
<div class="abs hero" role="img" aria-label="Abstract glowing green and violet data wave on a dark blue background"></div>
<h1 class="abs hero-title" style="left:90px;top:222px;font-family:'Cinzel',serif;font-weight:400;font-size:64px;line-height:62px;color:#fff">Halvern Ridge<br>Advisory LLC</h1>
<a class="abs btn" style="left:90px;top:366px;width:196px;height:52px;font-size:20px">Get Started</a>
<div class="abs dots"><span></span><span></span><span></span><span></span></div>

<!-- services -->
<div class="abs service" style="left:52px">
  <svg width="54" height="54" viewBox="0 0 54 54" fill="none" stroke="#888" stroke-width="1.6"><circle cx="27" cy="27" r="12"/><circle cx="27" cy="27" r="5"/><path d="M27 6v7M27 41v7M6 27h7M41 27h7M12 12l5 5M37 37l5 5M42 12l-5 5M17 37l-5 5"/></svg>
  IT<br>Services</div>
<div class="abs divider" style="left:243px"></div>
<div class="abs service" style="left:273px">
  <svg width="54" height="54" viewBox="0 0 54 54" fill="none" stroke="#888" stroke-width="1.6"><rect x="10" y="10" width="34" height="24" rx="2"/><path d="M4 42h46l-4-8H8z"/></svg>
  Cyber<br>Security</div>
<div class="abs divider" style="left:460px"></div>
<div class="abs service" style="left:495px">
  <svg width="54" height="54" viewBox="0 0 54 54" fill="none" stroke="#888" stroke-width="1.6"><circle cx="27" cy="24" r="10"/><path d="M27 14v-8M27 34v6M17 24h-8M45 24h-8M10 48l8-10M44 48l-8-10M18 48h18"/></svg>
  Risk<br>Management</div>
<div class="abs divider" style="left:693px"></div>
<div class="abs service" style="left:715px">
  <svg width="54" height="54" viewBox="0 0 54 54" fill="none" stroke="#888" stroke-width="1.6"><rect x="12" y="6" width="34" height="42" rx="2"/><path d="M19 16h20M19 24h20M19 32h12"/><circle cx="12" cy="40" r="7"/></svg>
  Project<br>Management</div>
<div class="abs svc-card">
  <div class="media" role="img" aria-label="Business analytics icons over a blue tinted photo of hands at work"></div>
  <p>Data Analytics<br>Consulting</p>
</div>

<!-- welcome -->
<section class="abs welcome">
  <h2>Welcome To Halvern Ridge Advisory LLC</h2>
  <p>Lorem ipsum dolor sit amet, consectetur adipiscing elit, sed do eiusmod tempor incididunt ut labore et dolore magna aliqua. Ut enim ad minim veniam, quis nostrud exercitation ullamco laboris nisi ut aliquip ex ea commodo consequat. Duis aute irure dolor in reprehenderit in voluptate velit esse cillum dolore eu fugiat nulla pariatur. Excepteur sint occaecat cupidatat non proident, sunt in culpa qui officia deserunt mollit anim id est laborum.</p>
  <p>Sed ut perspiciatis unde omnis iste natus error sit voluptatem accusantium doloremque laudantium, totam rem aperiam, eaque ipsa quae ab illo inventore<br>veritatis et quasi architecto beatae vitae dicta sunt explicabo.</p>
  <a class="btn" style="width:196px;height:55px;margin:0 auto;font-size:20px">Read More</a>
</section>

<!-- about -->
<section class="abs about">
  <h2>About Us</h2>
  <p>Lorem ipsum dolor sit amet, consectetur adipiscing elit, sed do eiusmod tempor incididunt ut labore et dolore magna aliqua. Ut enim ad minim veniam, quis nostrud exercitation ullamco laboris nisi ut aliquip ex ea commodo consequat. Duis aute irure dolor in reprehenderit in voluptate velit esse cillum dolore eu fugiat nulla pariatur. Excepteur sint occaecat cupidatat non proident, sunt in culpa qui officia deserunt mollit anim id est laborum</p>
  <svg width="40" height="12" viewBox="0 0 40 12"><path d="M0 6h37M32 1l5 5-5 5" stroke="#fff" stroke-width="1.6" fill="none"/></svg>
</section>
<div class="abs about-photo" role="img" aria-label="Person pointing at a project schedule chart on a desktop monitor"></div>

<!-- testimonials -->
<h2 class="abs section-title" style="top:1875px">Testimonials</h2>
<div class="abs arrow" style="left:80px">&#8249;</div>
<div class="abs arrow" style="left:1110px">&#8250;</div>
<article class="abs t-card" style="left:141px;width:288px">
  <div class="media" role="img" aria-label="Hand touching a laptop showing blue analytics charts" style="background:linear-gradient(135deg,#3a3f46,#1c3c6b 55%,#6f6a66)">
    <p class="quote">“Lorem ipsum dolor sit amet, consectetur adipiscing elit, sed do eiusmod tempor incididunt ut labore et dolore magna aliqua.”</p>
  </div>
  <div class="who"><span class="av" role="img" aria-label="Client portrait"></span><span>Colin M.<i>Duluth, GA</i></span></div>
  <p class="date">Added on 01/21/2020 09:27:24 pm</p>
</article>
<article class="abs t-card" style="left:453px;width:296px">
  <div class="media" role="img" aria-label="Hands typing on a keyboard with a digital network overlay" style="background:linear-gradient(135deg,#b9c7d8,#5e7896 55%,#2f4560)">
    <p class="quote">“Lorem ipsum dolor sit amet, consectetur adipiscing elit, sed do”</p>
  </div>
  <div class="who"><span class="av" role="img" aria-label="Client portrait"></span><span>Nadia F.<i>North Las Vegas, NV</i></span></div>
  <p class="date">Added on 01/21/2020 09:19:30 pm</p>
</article>
<article class="abs t-card" style="left:770px;width:289px">
  <div class="media" role="img" aria-label="Two colleagues discussing work at a computer in an office" style="background:linear-gradient(135deg,#8a5a3a,#4b3b33 50%,#2b2f36)">
    <p class="quote">“Lorem ipsum dolor sit amet, consectetur adipiscing elit, sed do eiusmod tempor incididunt ut labore et dolore magna aliqua.”</p>
  </div>
  <div class="who"><span class="av" role="img" aria-label="Client portrait"></span><span>Owen T.<i>Flagstaff, AZ</i></span></div>
  <p class="date">Added on 01/21/2020 09:03:06 pm</p>
</article>

<!-- ready -->
<div class="abs ready-photo" role="img" aria-label="Analyst working at several monitors showing blue data visualisations"></div>
<section class="abs ready">
  <h2>Ready to get<br>started?</h2>
  <p>Sed ut perspiciatis unde omnis iste natus error sit voluptatem</p>
  <a class="btn" style="width:165px;height:49px;font-size:15px">Get Started</a>
</section>

<!-- blog -->
<h2 class="abs section-title" style="top:2988px">Latest Blog</h2>
<article class="abs post" style="left:90px">
  <div class="media" role="img" aria-label="Laptop keyboard with glowing blue digital interface" style="background:linear-gradient(135deg,#0d1c3a,#24487a 60%,#0a1428)"></div>
  <h3>Lorem ipsum dolor sit</h3><div class="bar"></div>
  <p>Lorem ipsum dolor sit amet, consectetur aing elit, sed do eiusmod tempor incididunt ut labore et dolore magna aliqua.</p>
  <a class="more">Read More &raquo;</a>
</article>
<article class="abs post" style="left:437px">
  <div class="media" role="img" aria-label="Professional reviewing a dashboard on a laptop in a bright office" style="background:linear-gradient(135deg,#c9d3cd,#6e8592 55%,#2c3a4a)"></div>
  <h3>Lorem ipsum dolor sit</h3><div class="bar"></div>
  <p>Lorem ipsum dolor sit amet, consectetur aing elit, sed do eiusmod tempor incididunt ut labore et dolore magna aliqua.</p>
  <a class="more">Read More &raquo;</a>
</article>
<article class="abs post" style="left:783px">
  <div class="media" role="img" aria-label="Team reviewing printed charts and a tablet on a desk" style="background:linear-gradient(135deg,#e9e4dc,#b8a795 50%,#3e4b63)"></div>
  <h3>Lorem ipsum dolor sit amet, consectetur adipisc</h3><div class="bar"></div>
  <p>Lorem ipsum dolor sit amet, consectetur aing elit, sed do eiusmod tempor incididunt ut labore</p>
  <a class="more">Read More &raquo;</a>
</article>

<!-- footer -->
<footer class="abs footer"></footer>
<div class="abs f-col" style="left:90px;width:250px">
  <h4>RECENT NEWS</h4>
  <div class="news"><span class="thumb" role="img" aria-label="News photo"></span><span>Lorem ipsum dolor sit amet, consectetur<small>Jan 12,2020</small></span></div>
  <div class="news"><span class="thumb" role="img" aria-label="News photo"></span><span>Lorem ipsum dolor sit amet, consectetur<small>Jan 12,2020</small></span></div>
</div>
<div class="abs f-col f-links" style="left:367px">
  <h4>USEFULL LINKS</h4>
  Home<br>About Halvern<br>Our Experts<br>News And Events<br>Careers<br>Contact Us
</div>
<div class="abs f-col" style="left:569px;width:260px">
  <h4>NEWSLETTER</h4>
  Lorem ipsum dolor sit amet,<br>consectetur
  <div class="nl-form"><span>Email Address</span><b><svg width="18" height="18" viewBox="0 0 24 24"><path d="M2 12l20-9-7 19-4-8z" fill="#fff"/></svg></b></div>
  <div class="f-social"><span></span><span></span><span></span></div>
</div>
<div class="abs f-col" style="left:873px;width:237px">
  <h4>CONTACT US</h4>
  <div class="c-line">Lorem ipsum dolor sit amet,<br>consectetur</div>
  <div class="c-line"><svg width="10" height="14" viewBox="0 0 10 14"><path d="M5 0a5 5 0 0 1 5 5c0 4-5 9-5 9S0 9 0 5a5 5 0 0 1 5-5z" fill="#fff"/><circle cx="5" cy="5" r="2" fill="#161616"/></svg><span>14 Alder Crest Rd, Marlow Falls,<br>PA 17402</span></div>
  <div class="c-line"><svg width="12" height="12" viewBox="0 0 24 24"><path d="M6.6 10.8a15 15 0 0 0 6.6 6.6l2.2-2.2c.3-.3.7-.4 1-.2 1.1.4 2.3.6 3.6.6.6 0 1 .4 1 1V20c0 .6-.4 1-1 1A17 17 0 0 1 3 4c0-.6.4-1 1-1h3.5c.6 0 1 .4 1 1 0 1.3.2 2.5.6 3.6.1.3 0 .7-.2 1z" fill="#fff"/></svg>+1 555 010 2040</div>
  <div class="c-line"><svg width="14" height="11" viewBox="0 0 18 14"><rect width="18" height="14" rx="2" fill="#fff"/><path d="M1 2l8 6 8-6" stroke="#161616" stroke-width="1.6" fill="none"/></svg>hello@halvernridge.example</div>
</div>
<p class="abs copyright">&copy; Copyrights.2021.The Company name</p>

</body>
</html>
```